HVAC company business card design

We need a business card design for a HVAC company. The design must look professional. Both sides will be used. The total data to be on the business card is
Name
Position
Email
Direct Phone/Moile Phone
Company Contacts /Address, Phone, Fax, web)
All data will be submit once the design is confirmed. For generic purposes use;
Cem Orkut
Managing Director
+905124418352 (Mobile)
4718 Sokak No: 9 KGTB Denizkoy ARVALI KESTRA
Tel: +905124418352 Fax : +905124418359
www.ozkivra.com.tr

Target Market(s)

HVAC

Industry/Entity Type

Business

Contact Information for Business Card

The total data to be on the business card is
Name
Position
Email
Direct Phone/Moile Phone
Cem Orkut
Managing Director
+905124418352 (Mobile)
www.ozkivra.com.tr
The BC will use both sides of the card. The front will include the full logo and the details for the business card holder. The business card can be divided into vertical/horizontal or to a special shape. The common data like the company address/phone/fax should be indicated elsewehere. The back can contain some part or the whole logo and must contain the web address.

Font styles to use
Serif
Sans Serif

Colors
0355a3
cfdfed

Requirements
Should not have
• Please be careful with the fonts, it shouldnt be too small or too big and must not interfere with the logo fonts. If you need to use a curvy shape please do not use as the logo is already curvy or use the curves from the logo (if it looks good, otherwise forget it)
• We are not in favor of pictograms, only if they are perfect use them.

```html
<!DOCTYPE html>
<html lang="en">
<head>
<meta charset="utf-8">
<title>Ozkivra business card – front and back</title>
<link href="https://fonts.googleapis.com/css2?family=Play:wght@400;700&display=swap" rel="stylesheet">
<style>
  :root{
    --stage:#8d8d8d;
    --paper:#eef0f3;
    --ink:#2b3448;
    --blue:#0355a3;
    --blue-bright:#2f73cf;
    --blue-deep:#1d56b4;
    --band-line:#1b2a4a;
    --divider:#c4c8cf;
    --pale:#cfdfed;
  }
  *{margin:0;padding:0;box-sizing:border-box}
  html,body{width:1105px;height:1200px;overflow:hidden}
  body{background:var(--stage);font-family:"Play",sans-serif;position:relative}

  .card{position:absolute;left:182px;width:746px;height:427px;overflow:hidden}
  .card--front{top:119px;background:var(--paper)}
  .card--back{top:637px;background:radial-gradient(ellipse at 45% 35%,var(--blue-bright) 0%,var(--blue-deep) 75%)}

  /* front */
  .brand{position:absolute;left:66px;top:196px;display:flex;align-items:center;gap:14px}
  .brand__dot{width:48px;height:48px;border-radius:50%;background:var(--blue)}
  .brand__name{font-size:46px;font-weight:700;color:var(--ink);letter-spacing:1px;line-height:1}

  .divider{position:absolute;left:393px;top:102px;width:1px;height:262px;background:var(--divider)}

  .holder{position:absolute;left:425px;top:104px;color:var(--ink)}
  .holder__name{font-size:25px;font-weight:700;color:var(--blue);line-height:30px}
  .holder__role{font-size:19px;line-height:26px}
  .holder__address{margin-top:10px;font-size:18.5px;line-height:30px;padding-left:3px}

  .contacts{list-style:none;margin-top:6px;padding-left:4px}
  .contacts li{display:flex;align-items:center;gap:12px;height:28px;font-size:18.5px;letter-spacing:1px}
  .contacts svg{width:17px;height:17px;fill:var(--blue)}
  .contacts .web{letter-spacing:0;font-size:18px}

  .band{position:absolute;left:0;bottom:0;width:100%;height:35px;
        background:linear-gradient(90deg,var(--blue-deep),#3f86db 55%,var(--blue-deep));
        border-top:3px solid var(--band-line)}

  /* back */
  .halo{position:absolute;left:180px;top:0;width:340px;height:340px;border-radius:50%;
        background:rgba(255,255,255,.07)}
  .back-name{position:absolute;left:0;right:0;top:172px;text-align:center;
             font-size:64px;font-weight:700;color:#fff;letter-spacing:2px;line-height:1}
  .back-web{position:absolute;left:0;right:0;top:265px;text-align:center;
            font-size:18px;letter-spacing:5px;color:var(--pale)}
</style>
</head>
<body>

<section class="card card--front" aria-label="Card front">
  <div class="brand">
    <span class="brand__dot"></span>
    <span class="brand__name">OZKIVRA</span>
  </div>

  <div class="divider"></div>

  <div class="holder">
    <p class="holder__name">Cem Orkut</p>
    <p class="holder__role">Managing Director</p>
    <p class="holder__address">4718 Sokak No: 9 KGTB<br>Denizkoy ARVALI KESTRA</p>
    <ul class="contacts">
      <li>
        <svg viewBox="0 0 24 24" aria-hidden="true"><path d="M6.6 10.8a15.1 15.1 0 0 0 6.6 6.6l2.2-2.2c.3-.3.7-.4 1-.2 1.1.4 2.3.6 3.6.6.6 0 1 .4 1 1V20c0 .6-.4 1-1 1A17 17 0 0 1 3 4c0-.6.4-1 1-1h3.5c.6 0 1 .4 1 1 0 1.3.2 2.5.6 3.6.1.3 0 .7-.2 1z"/></svg>
        <span>+905124418352</span>
      </li>
      <li>
        <svg viewBox="0 0 24 24" aria-hidden="true"><path d="M7 1h10a2 2 0 0 1 2 2v18a2 2 0 0 1-2 2H7a2 2 0 0 1-2-2V3a2 2 0 0 1 2-2zm0 3v14h10V4zm5 15.5a1 1 0 1 0 0 2 1 1 0 0 0 0-2z"/></svg>
        <span>+905124418352</span>
      </li>
      <li>
        <svg viewBox="0 0 24 24" aria-hidden="true"><path d="M7 2h9l3 3v4h1a2 2 0 0 1 2 2v7a2 2 0 0 1-2 2h-2v3H6v-3H4a2 2 0 0 1-2-2v-7a2 2 0 0 1 2-2h3zm2 2v5h8V6h-2V4zM8 16v5h8v-5z"/></svg>
        <span>+905124418359</span>
      </li>
      <li>
        <svg viewBox="0 0 24 24" aria-hidden="true"><path d="M12 2a10 10 0 1 0 0 20 10 10 0 0 0 0-20zm-1 17.9A8 8 0 0 1 4.2 10L9 14.8V16a2 2 0 0 0 2 2zm6.9-2.6A2 2 0 0 0 16 16h-1v-3a1 1 0 0 0-1-1H8v-2h2a1 1 0 0 0 1-1V7h2a2 2 0 0 0 2-2v-.4a8 8 0 0 1 2.9 12.7z"/></svg>
        <span class="web">www.ozkivra.com.tr</span>
      </li>
    </ul>
  </div>

  <div class="band"></div>
</section>

<section class="card card--back" aria-label="Card back">
  <div class="halo"></div>
  <p class="back-name">OZKIVRA</p>
  <p class="back-web">www.ozkivra.com.tr</p>
</section>

</body>
</html>
```